Driving School Business card design

Hi, we are starting a new business (Driving School) and would like your help with our business card design.
We are located in Adelaide SA.
Our aim is to help young people achieve best possible results by promoting safe and stress free driving.

Name of our school is "Velmira" which means best or most favorable.

Hope there is someone out there in wonderful world of design who can think outside of square and give us recognizable/ unique business card design.

Target Market(s)

16+

Industry/Entity Type

Business

Contact Information for Business Card

Name of our business is "Velmira driver training"
Our idea is to make letter "L' in Velmira more distinct (noticeable) by different color or font, so it gets associated with learner driver.
We like combination of white, dark gray and yellow but do not limit our self to that.
Reverse side of our card would have to incorporate writing space for date and time of the next lesson.

Requirements
Must have
• Business name: Velmira driver training
• Owner/ instructor name
• Mobile no:
• Chatterloop logo
Should not have
• Anything Not associated with driving

```html
<!DOCTYPE html>
<html lang="en">
<head>
<meta charset="utf-8">
<title>Velmira Driver Training — Business Card</title>
<link href="https://fonts.googleapis.com/css2?family=Open+Sans:wght@400;600;700;800&display=swap" rel="stylesheet">
<style>
  :root {
    --page: #e9e8e6;
    --card-white: #ffffff;
    --slate: #3f4a4e;
    --ink: #2a2f31;
    --rule: #9a9a9a;
    --asphalt-dark: #202426;
    --asphalt-mid: #33393b;
    --yellow: #f2c21b;
    --white: #ffffff;
  }
  * { margin: 0; padding: 0; box-sizing: border-box; }
  html, body { width: 1200px; height: 1200px; overflow: hidden; }
  body {
    background: var(--page);
    font-family: "Open Sans", Arial, sans-serif;
    position: relative;
  }
  .card {
    position: absolute;
    width: 700px;
    height: 400px;
    border-radius: 18px;
    overflow: hidden;
  }

  /* ---------- Reverse side: lesson schedule ---------- */
  .card-back {
    left: 130px;
    top: 150px;
    background: var(--card-white);
    box-shadow: 0 6px 18px rgba(0,0,0,0.18);
  }
  .schedule {
    position: absolute;
    top: 36px;
    left: 44px;
    right: 44px;
    display: grid;
    grid-template-columns: 280px 140px 1fr;
    column-gap: 20px;
  }
  .col-label {
    display: block;
    font-weight: 700;
    font-size: 19px;
    line-height: 24px;
    color: var(--ink);
  }
  .write-line {
    height: 36px;
    border-bottom: 1px solid var(--rule);
  }
  .social-band {
    position: absolute;
    left: 0;
    bottom: 36px;
    width: 340px;
    height: 64px;
    background: var(--slate);
    border-radius: 0 18px 18px 0;
    display: flex;
    align-items: center;
    padding-left: 44px;
    gap: 14px;
  }
  .social-mark {
    width: 28px; height: 28px;
    flex: none;
    background: var(--white);
    border-radius: 4px;
  }
  .social-handle {
    color: var(--white);
    font-size: 15px;
    font-weight: 600;
    letter-spacing: 0.2px;
    white-space: nowrap;
  }
  .brand-back {
    position: absolute;
    right: 34px;
    bottom: 38px;
    color: var(--slate);
    font-weight: 800;
    line-height: 0.95;
    white-space: nowrap;
  }
  .brand-back .brand-name { font-size: 56px; letter-spacing: 2px; display: block; }
  .brand-back .brand-tag { font-size: 30px; letter-spacing: 1px; display: block; }

  /* ---------- Front side: contact ---------- */
  .card-front {
    left: 380px;
    top: 640px;
    box-shadow: 0 6px 18px rgba(0,0,0,0.25);
  }
  .road-photo {
    position: absolute; inset: 0;
    background: radial-gradient(ellipse at 70% 40%, var(--asphalt-mid), var(--asphalt-dark));
  }
  .front-content {
    position: absolute;
    right: 34px;
    top: 34px;
    text-align: right;
    color: var(--white);
  }
  .brand-front { font-weight: 800; line-height: 0.95; text-align: left; color: var(--white); white-space: nowrap; }
  .brand-front .brand-name { font-size: 66px; letter-spacing: 2px; display: block; }
  .brand-front .brand-tag { font-size: 35px; letter-spacing: 1px; display: block; }
  .owner-name {
    margin-top: 22px;
    color: var(--yellow);
    font-weight: 800;
    font-size: 27px;
    letter-spacing: 1px;
  }
  .owner-role { font-size: 15px; letter-spacing: 0.5px; margin-top: 2px; }
  .contact-list { list-style: none; margin-top: 10px; }
  .contact-item {
    font-size: 15.5px;
    display: flex;
    justify-content: flex-end;
    align-items: center;
    gap: 8px;
    height: 25px;
  }
  .contact-icon { width: 17px; height: 17px; flex: none; }
  .address {
    margin-top: 12px;
    color: var(--yellow);
    font-weight: 700;
    font-size: 16px;
    line-height: 1.25;
    letter-spacing: 0.3px;
  }
</style>
</head>
<body>

<section class="card card-back" aria-label="Reverse side with next lesson schedule">
  <div class="schedule">
    <div class="schedule-col">
      <span class="col-label">Next Lesson</span>
      <div class="write-line"></div><div class="write-line"></div><div class="write-line"></div><div class="write-line"></div><div class="write-line"></div>
    </div>
    <div class="schedule-col">
      <span class="col-label">Date</span>
      <div class="write-line"></div><div class="write-line"></div><div class="write-line"></div><div class="write-line"></div><div class="write-line"></div>
    </div>
    <div class="schedule-col">
      <span class="col-label">Time</span>
      <div class="write-line"></div><div class="write-line"></div><div class="write-line"></div><div class="write-line"></div><div class="write-line"></div>
    </div>
  </div>

  <div class="social-band">
    <span class="social-mark" aria-hidden="true"></span>
    <span class="social-handle">VELMIRA_DRIVER_TRAINING</span>
  </div>

  <div class="brand-back">
    <span class="brand-name">VELMIRA</span>
    <span class="brand-tag">DRIVER TRAINING</span>
  </div>
</section>

<section class="card card-front" aria-label="Front side with contact details">
  <div class="road-photo" role="img" aria-label="Close-up of dark asphalt road with two yellow centre lines"></div>
  <div class="front-content">
    <div class="brand-front">
      <span class="brand-name">VELMIRA</span>
      <span class="brand-tag">DRIVER TRAINING</span>
    </div>
    <div class="owner-name">DANIEL ASHCOMBE</div>
    <div class="owner-role">DIRECTOR</div>
    <ul class="contact-list">
      <li class="contact-item">555-014-2297
        <svg class="contact-icon" viewBox="0 0 20 20" aria-hidden="true"><rect width="20" height="20" rx="3" fill="#f2c21b"/><path d="M6 4.5l2 .3 1 3-1.4 1.2a8 8 0 003.4 3.4l1.2-1.4 3 1 .3 2c-.3 1-1.3 1.5-2.3 1.4A10 10 0 014.6 6.8C4.5 5.8 5 4.8 6 4.5z" fill="#202426"/></svg>
      </li>
      <li class="contact-item">daniel@velmiradrivertraining.com
        <svg class="contact-icon" viewBox="0 0 20 20" aria-hidden="true"><rect width="20" height="20" rx="3" fill="#f2c21b"/><rect x="4" y="6" width="12" height="8" rx="1" fill="#202426"/><path d="M4.5 6.5l5.5 4 5.5-4" stroke="#f2c21b" stroke-width="1.2" fill="none"/></svg>
      </li>
      <li class="contact-item">www.velmiradrivertraining.com
        <svg class="contact-icon" viewBox="0 0 20 20" aria-hidden="true"><rect width="20" height="20" rx="3" fill="#f2c21b"/><circle cx="10" cy="10" r="6" fill="none" stroke="#202426" stroke-width="1.4"/><ellipse cx="10" cy="10" rx="2.6" ry="6" fill="none" stroke="#202426" stroke-width="1.2"/><path d="M4 10h12" stroke="#202426" stroke-width="1.2"/></svg>
      </li>
    </ul>
    <div class="address">48 HARBOUR LANE<br>GLENMORE, SA 5061</div>
  </div>
</section>

</body>
</html>
```